Professional Website

We are looking for a new website for our Staffing Company. Attached is a document with all the details and pages needed along with some examples of others websites.

We want a professional Look and feel around the same color theme as the attached Vivid Vision.

We currently host our site on SiteKarn.io. If the winning designer can also add to SiteKarn, that is a plus.

```html
<!DOCTYPE html>
<html lang="en">
<head>
<meta charset="utf-8">
<title>CrewBridge — Recruiting Agency</title>
<link href="https://fonts.googleapis.com/css2?family=Poppins:wght@400;500;600;700&family=Roboto:wght@700&display=swap" rel="stylesheet">
<style>
:root{
  --blue:#2741c4;
  --blue-deep:#1f3bbf;
  --blue-soft:#6d85e6;
  --blue-pale:#c9d1f4;
  --ink:#111;
  --text:#333;
  --dark:#1c1c1c;
  --white:#fff;
}
*{margin:0;padding:0;box-sizing:border-box}
html,body{width:717px;height:1200px;overflow:hidden;background:var(--white);font-family:'Poppins',sans-serif;color:var(--text)}
.page{position:relative;width:717px;height:1200px}
.abs{position:absolute}

/* header */
.header{position:absolute;left:0;top:0;width:717px;height:65px;background:var(--white)}
.brand{position:absolute;left:59px;top:12px;display:flex;align-items:center;gap:6px;font-weight:700;font-size:27px;color:var(--blue);letter-spacing:-.5px}
.brand .mark{width:12px;height:12px;background:var(--blue)}
.logins{position:absolute;left:297px;top:9px;display:flex;gap:4px}
.login{width:89px;height:25px;border:1px solid var(--blue);border-radius:2px;color:var(--blue);font-size:7.8px;font-weight:500;display:flex;align-items:center;justify-content:center;white-space:nowrap;letter-spacing:-.2px}
.hotline-top{position:absolute;left:574px;top:10px;display:flex;gap:5px;align-items:center;color:var(--blue);font-size:8.5px;line-height:11px;font-weight:500}
.nav{position:absolute;left:296px;top:47px;width:362px;display:flex;justify-content:space-between;font-size:8.5px;font-weight:500;color:var(--ink)}

/* hero */
.hero{position:absolute;left:0;top:65px;width:717px;height:405px;background:var(--blue-deep);overflow:hidden}
.hero .deco{position:absolute;background:rgba(255,255,255,.14);border-radius:10px}
.vertical-name{position:absolute;left:17px;top:292px;transform:rotate(-90deg);transform-origin:left top;font-family:'Roboto',sans-serif;font-size:28px;line-height:28px;font-weight:700;color:rgba(255,255,255,.3);letter-spacing:1px;white-space:nowrap}
.hero h1{position:absolute;left:81px;top:152px;font-family:'Roboto',sans-serif;font-size:23.5px;line-height:31.5px;color:var(--white);font-weight:700}
.hero .cta{position:absolute;left:75px;top:263px;width:123px;height:26px;border-radius:13px;background:var(--white);color:var(--blue);font-family:'Roboto',sans-serif;font-weight:700;font-size:9px;display:flex;align-items:center;justify-content:center}
.chip{position:absolute;width:119px;height:31px;border:1px solid rgba(255,255,255,.7);border-radius:16px;color:var(--white);background:var(--blue-deep)}
.chip b{position:absolute;top:6px;font-size:7px;font-weight:600}
.chip i{position:absolute;top:5px;font-style:normal;font-size:7px}
.chip small{position:absolute;top:19px;font-size:5px;white-space:nowrap}
.chip .dot{position:absolute;top:3px;width:25px;height:25px;border-radius:50%;background:#e6e6e6}

/* cards */
.card{position:absolute;top:513px;width:268px;height:225px;background:var(--white);box-shadow:0 2px 10px rgba(0,0,0,.12);text-align:center}
.card h2,.card p,.card .card-link{position:absolute;left:0;width:100%;display:block}
.card h2{top:146px;font-size:16.5px;font-weight:600;color:var(--ink)}
.card p{top:178px;font-size:8.7px}
.card .card-link{top:196px;font-size:9.5px;font-weight:600;color:var(--blue);text-decoration:none}

/* about */
.about h2{position:absolute;left:59px;top:812px;font-size:23px;font-weight:700;color:var(--ink)}
.about p{position:absolute;left:60px;top:853px;width:290px;font-size:8.8px;letter-spacing:-.15px;line-height:18.3px}
.quote{position:absolute;left:557px;top:850px;font-size:8.5px;line-height:12px;font-weight:500;color:#333}

/* footer */
.footer{position:absolute;left:0;top:1044px;width:717px;height:156px;background:var(--dark);color:var(--white)}
.footer .brand{left:59px;top:22px;color:var(--white);font-size:36px}
.footer .brand .mark{background:var(--white);width:14px;height:14px}
.areas{position:absolute;left:367px;top:26px;font-size:8.7px;line-height:15.5px}
.areas h3{font-size:10px;font-weight:600;margin-bottom:4px}
.hotline-foot{position:absolute;left:543px;top:30px}
.hotline-foot h3{font-size:10px;font-weight:600}
.hotline-foot div{font-size:14.5px}
.footer hr{position:absolute;left:59px;top:117px;width:599px;border:0;border-top:1px solid #3a3a3a}
.copy{position:absolute;top:133px;width:100%;text-align:center;font-size:9.5px}
</style>
</head>
<body>
<div class="page">

<header class="header">
  <div class="brand"><span class="mark"></span>CrewBridge</div>
  <div class="logins">
    <div class="login">Employee Login</div>
    <div class="login">QuickPay Card Login</div>
    <div class="login">Harbor Bank Login</div>
  </div>
  <div class="hotline-top">
    <svg width="16" height="16" viewBox="0 0 24 24" fill="none" stroke="#2741c4" stroke-width="1.6"><path d="M5 3h4l2 5-3 2a11 11 0 0 0 6 6l2-3 5 2v4a2 2 0 0 1-2 2A17 17 0 0 1 3 5a2 2 0 0 1 2-2z"/></svg>
    <div>Hotline #<br>555-014-2290</div>
  </div>
  <nav class="nav"><span>HOME</span><span>|</span><span>ABOUT</span><span>|</span><span>JOB ⌄</span><span>|</span><span>OFFICE INFO</span><span>|</span><span>CONTACT US</span></nav>
</header>

<section class="hero">
  <div class="deco" style="left:-10px;top:10px;width:56px;height:55px"></div>
  <div class="deco" style="left:189px;top:72px;width:27px;height:27px;border-radius:50%"></div>
  <div class="deco" style="left:106px;top:312px;width:51px;height:48px"></div>
  <div class="deco" style="left:626px;top:278px;width:50px;height:48px"></div>
  <div class="deco" style="left:653px;top:186px;width:26px;height:26px"></div>
  <div class="deco" style="left:247px;top:272px;width:110px;height:140px;border-radius:40px"></div>
  <div class="vertical-name">CREWBRIDGE</div>
  <h1>RECRUITING AGENCY<br>FOR TEMPORARY AND<br>DIRECT HIRE EMPLOYEES</h1>
  <div class="cta">JOB OPPORTUNITIES</div>

  <svg class="abs" style="left:0;top:0" width="717" height="405">
    <circle cx="496" cy="177" r="96" fill="none" stroke="#fff" stroke-width="1"/>
    <circle cx="497" cy="81" r="4" fill="#fff"/>
    <circle cx="413" cy="222" r="4" fill="#fff"/>
  </svg>

  <div class="abs" role="img" aria-label="Smiling young man sitting cross-legged with a laptop" style="left:375px;top:120px;width:230px;height:285px;border-radius:100px 100px 60px 60px;background:linear-gradient(#b45a4e,#d8cbb6)"></div>
  <div class="abs" role="img" aria-label="Potted green plant" style="left:282px;top:245px;width:88px;height:160px;border-radius:40px 40px 10px 10px;background:linear-gradient(#2f6b2a,#e9e9e9)"></div>
  <div class="abs" role="img" aria-label="White coffee mug" style="left:610px;top:340px;width:48px;height:50px;border-radius:6px;background:#e8e8ea"></div>

  <div class="chip" style="left:363px;top:85px"><b style="left:5px">Job Title</b><i style="left:57px">○circle</i><small style="left:9px">Lorem ipsum dolor sit amet</small><span class="dot" style="right:3px"></span></div>
  <div class="chip" style="left:525px;top:85px"><span class="dot" style="left:3px"></span><b style="left:33px">Job Title</b><i style="left:85px">○circle</i><small style="left:32px">Lorem ipsum dolor sit amet</small></div>
  <div class="chip" style="left:322px;top:138px"><b style="left:5px">Job Title</b><i style="left:57px">○circle</i><small style="left:9px">Lorem ipsum dolor sit amet</small><span class="dot" style="right:3px"></span></div>
  <div class="chip" style="left:566px;top:138px"><span class="dot" style="left:3px"></span><b style="left:33px">Job Title</b><i style="left:85px">○circle</i><small style="left:32px">Lorem ipsum dolor sit amet</small></div>

  <svg class="abs" style="left:0;top:330px" width="717" height="75" viewBox="0 0 717 75" preserveAspectRatio="none">
    <path d="M0 25 C90 5 200 20 280 45 C300 55 330 60 360 60 L717 60 L717 75 L0 75Z" fill="#a9b6ee"/>
    <path d="M0 45 C110 30 220 70 290 75 L0 75Z" fill="#dfe4f8"/>
    <path d="M600 40 C650 45 690 55 717 62 L717 75 L590 75Z" fill="#c9d1f4"/>
  </svg>
</section>

<div class="card" style="left:76px">
  <svg class="abs" style="left:78px;top:16px" width="112" height="112" viewBox="0 0 112 112">
    <circle cx="56" cy="56" r="56" fill="#cdd3f1"/><circle cx="56" cy="56" r="49" fill="#6d7fd8"/><circle cx="56" cy="56" r="42" fill="#2741c4"/>
    <g fill="none" stroke="#fff" stroke-width="1.6"><rect x="36" y="42" width="40" height="30" rx="2"/><path d="M47 42v-4h18v4M36 55h40"/><rect x="53" y="52" width="6" height="6"/></g>
  </svg>
  <h2>I’m looking for a Job</h2>
  <p>At vero eos et accusamus et iusto odio dignissimos</p>
  <a class="card-link">Contact Us Today ⟶</a>
</div>
<div class="card" style="left:373px">
  <svg class="abs" style="left:78px;top:16px" width="112" height="112" viewBox="0 0 112 112">
    <circle cx="56" cy="56" r="56" fill="#cdd3f1"/><circle cx="56" cy="56" r="49" fill="#6d7fd8"/><circle cx="56" cy="56" r="42" fill="#2741c4"/>
    <g fill="none" stroke="#fff" stroke-width="1.6"><circle cx="56" cy="42" r="8"/><path d="M40 78v-12a10 10 0 0 1 10-10h12a10 10 0 0 1 10 10v12M56 56l-3 14 3 4 3-4-3-14"/></g>
  </svg>
  <h2>I need Employees</h2>
  <p>At vero eos et accusamus et iusto odio dignissimos</p>
  <a class="card-link">Contact Us Today ⟶</a>
</div>

<section class="about">
  <h2>CrewBridge</h2>
  <p>Greatest part of our daily job is that we are constantly bringing people together. Our Clients come to us in search of the perfect candidate and the job hunters approach us when they are in need of a job or looking for their next exciting role. Being able to work with and connect the two is incredibly satisfying. Not to mention that in today's current job market, employers are fighting for the top talent. This makes our employees and partners grateful for the help in finding it!</p>
  <svg class="abs" style="left:360px;top:800px" width="357" height="244">
    <path d="M40 220 C10 170 20 80 110 45 C200 10 300 60 310 150 C315 200 300 230 290 244 L50 244Z" fill="#ececef"/>
    <path d="M8 145 C5 90 40 65 90 60 C50 90 25 120 10 155Z" fill="#2741c4"/>
    <path d="M228 34 C270 2 330 12 357 30" fill="none" stroke="#2741c4" stroke-width="1.2"/>
    <path d="M290 228 C320 230 345 215 357 205" fill="none" stroke="#2741c4" stroke-width="1.2"/>
    <circle cx="305" cy="15" r="13" fill="#3b56d6"/>
  </svg>
  <div class="abs" role="img" aria-label="Smiling man in a blue shirt with arms crossed" style="left:415px;top:763px;width:130px;height:281px;border-radius:60px 60px 0 0;background:linear-gradient(#6b4a3a 0%,#d9b59c 25%,#9db6d6 45%,#8fa9cf 100%)"></div>
  <div class="quote">"CrewBridge helped me<br>land my dream job!"</div>
</section>

<footer class="footer">
  <div class="brand"><span class="mark"></span>CrewBridge</div>
  <div class="areas"><h3>Areas we service</h3>Maple Ridge<br>Oakfield<br>Riverton</div>
  <svg class="abs" style="left:501px;top:29px" width="34" height="34" viewBox="0 0 34 34"><circle cx="17" cy="17" r="17" fill="#2741c4"/><path d="M12 10h3l1.5 4-2 1.5a8 8 0 0 0 4 4l1.5-2 4 1.5v3a1.5 1.5 0 0 1-1.5 1.5A12.5 12.5 0 0 1 10.5 11.5 1.5 1.5 0 0 1 12 10z" fill="#fff"/></svg>
  <div class="hotline-foot"><h3>Hotline</h3><div># 555-014-2290</div></div>
  <hr>
  <div class="copy">©Copyright ©2022 crewbridge inc. All Rights Reserved.</div>
</footer>

</div>
</body>
</html>
```